Quarterly real estate newsletter

I need to update the layout of my newsletter so that the address can be printed on the newsletter itself. I also need to update the overall design. I need a template that I can use to edit the content going forward. This will be mailed to owners of homes worth $2,000,000 or more, so needs to be very polished and professional looking.
Below is the printer template that I need to use. Also is the last newsletter I sent, in Publisher format. The Cypress Report is a partial conversion to the new template, but still needs a lot of work. That is not how I want the final version to look.
On the cover, instead of a graph at the bottom, I would like a graphic with a few key market statistics (e.g. Median price, homes sold, average days on market) with some nice graphical elements, large arrows point up or down.
Inside I would like:
- an article with photos
- A list of recent solds
- our photo quiz
- a chart (like the one currently on the front)
- a second article (if there is room)
- contact info
The back is okay, although I think it could look a little cleaner
San Francisco home owners
Real Estate

```html
<!DOCTYPE html>
<html lang="en">
<head>
<meta charset="utf-8">
<title>The Cypress Report – Inside Spread</title>
<link href="https://fonts.googleapis.com/css2?family=Arimo:ital,wght@0,400;0,700;1,400&display=swap" rel="stylesheet">
<style>
:root{
  --navy:#4a5878;
  --title:#3d4a66;
  --ink:#2c2f36;
  --muted:#d2d4d8;
  --price:#d6e84a;
  --paper:#ffffff;
  --backdrop:#e9ecef;
  --rule:#c5ccd8;
}
*{margin:0;padding:0;box-sizing:border-box}
html,body{width:1200px;height:1200px;overflow:hidden;background:var(--backdrop);font-family:"Arimo",Arial,sans-serif;color:var(--ink)}
.spread{position:absolute;left:20px;top:161px;width:1160px;height:878px;background:var(--paper);box-shadow:0 2px 10px rgba(0,0,0,.12)}
.abs{position:absolute}
.page-title{font-weight:700;color:var(--title);font-size:28px;text-align:center;white-space:nowrap}
.body-copy{font-size:9.2px;line-height:1.42;text-align:justify}
.body-copy p+p{margin-top:12px}
.photo{position:absolute}
.interior{background:linear-gradient(135deg,#d9d6cf 0%,#8d8a84 45%,#f1efe9 70%,#6c6a66 100%)}
.house-dusk{background:linear-gradient(180deg,#6b86b8 0%,#9fb0cf 35%,#4a5470 65%,#e0a95c 85%,#3a3f4c 100%)}
.house-modern{background:linear-gradient(180deg,#cfd6e0 0%,#eef0f2 40%,#7f8894 65%,#2e3138 100%)}
.house-pool{background:linear-gradient(180deg,#8aa2c4 0%,#6f5a4a 40%,#d08a45 55%,#2d6a88 80%,#1f4a63 100%)}
.listings{left:10px;top:443px;width:545px;height:409px;display:grid;grid-template-columns:repeat(3,1fr);grid-template-rows:repeat(3,1fr);gap:3px 5px}
.tile{position:relative}
.tile .photo{left:0;top:0;right:0;bottom:28px}
.tile-caption{position:absolute;left:0;right:0;bottom:0;height:28px;background:var(--navy);text-align:center;font-weight:700;font-size:8.6px;line-height:1.25;padding-top:3px}
.tile-caption .area{color:#fff;display:block}
.tile-caption .price{color:var(--price);display:block}
.subtitle{font-style:italic;font-size:11px;text-align:center;color:var(--ink)}
.section-title{font-size:19px;font-weight:700;color:var(--title)}
.quiz{left:898px;top:462px;width:239px;height:258px;background:var(--navy);color:#fff;text-align:center}
.quiz h3{font-size:14px;font-weight:400;margin-top:8px}
.quiz .photo{left:11px;top:34px;width:120px;height:76px}
.quiz .prompt{position:absolute;left:10px;right:10px;top:134px;font-size:8.8px;line-height:1.4;text-align:left}
.quiz .submit{position:absolute;left:0;right:0;top:192px;font-size:8.8px}
.quiz .email{position:absolute;left:0;right:0;top:222px;font-size:11.5px;font-weight:700}
.contact{left:898px;top:729px;width:239px;height:114px;background:var(--muted);text-align:center;color:var(--title);font-size:8.6px;line-height:1.6;padding-top:10px}
.contact .name{font-size:11.5px;font-weight:700;margin-bottom:6px}
</style>
</head>
<body>
<div class="spread">

  <!-- Left page -->
  <h1 class="abs page-title" style="left:0;width:580px;top:22px">Your Article Title Here</h1>
  <div class="abs body-copy" style="left:25px;top:76px;width:270px">
    <p>Since 2012, San Francisco's overall average sales price has shown tremendous growth year over year. With San Francisco leading the charge after the 2008 market recession, available inventory dwindled and sales prices climbed annually throughout the City. However, second quarter 2016 data from the San Francisco Multiple Listing Service reflected that, while the San Francisco real estate market remains vibrant and strong, there has been a shift in direction.</p>
    <p>After seeing significant year-over-year gains, the average sales price throughout San Francisco for single-family homes fell slightly, 2.8 percent, decreasing from an average of $1.79 million in the second quarter of 2015, to an average of $1.74 million in the second quarter of 2016. In our review of seven major districts in the City, we found the average sales price in the second quarter of 2016 for a single-family home decreased in five of them, compared to the second quarter of 2015.</p>
  </div>
  <div class="photo interior" style="left:314px;top:79px;width:241px;height:114px" role="img" aria-label="Photo of a bright modern kitchen and living room"></div>
  <div class="photo house-dusk" style="left:314px;top:211px;width:241px;height:118px" role="img" aria-label="Photo of a two-storey house at dusk"></div>

  <h2 class="abs page-title" style="left:0;width:580px;top:393px">Daniel's Listings and Recent Sales</h2>
  <div class="abs listings">
    <div class="tile"><div class="photo house-dusk" role="img" aria-label="Listing photo: family house at dusk"></div><div class="tile-caption"><span class="area">Pacific Heights</span><span class="price">$11,000,000 2400 Maple</span></div></div>
    <div class="tile"><div class="photo house-modern" role="img" aria-label="Listing photo: modern white house"></div><div class="tile-caption"><span class="area">Pacific Heights</span><span class="price">$11,000,000 2400 Maple</span></div></div>
    <div class="tile"><div class="photo house-pool" role="img" aria-label="Listing photo: lit house with pool at evening"></div><div class="tile-caption"><span class="area">Pacific Heights</span><span class="price">$11,000,000 2400 Maple</span></div></div>
    <div class="tile"><div class="photo house-dusk" role="img" aria-label="Listing photo: family house at dusk"></div><div class="tile-caption"><span class="area">Pacific Heights</span><span class="price">$11,000,000 2400 Maple</span></div></div>
    <div class="tile"><div class="photo house-modern" role="img" aria-label="Listing photo: modern white house"></div><div class="tile-caption"><span class="area">Pacific Heights</span><span class="price">$11,000,000 2400 Maple</span></div></div>
    <div class="tile"><div class="photo house-pool" role="img" aria-label="Listing photo: lit house with pool at evening"></div><div class="tile-caption"><span class="area">Pacific Heights</span><span class="price">$11,000,000 2400 Maple</span></div></div>
    <div class="tile"><div class="photo house-dusk" role="img" aria-label="Listing photo: family house at dusk"></div><div class="tile-caption"><span class="area">Pacific Heights</span><span class="price">$11,000,000 2400 Maple</span></div></div>
    <div class="tile"><div class="photo house-modern" role="img" aria-label="Listing photo: modern white house"></div><div class="tile-caption"><span class="area">Pacific Heights</span><span class="price">$11,000,000 2400 Maple</span></div></div>
    <div class="tile"><div class="photo house-pool" role="img" aria-label="Listing photo: lit house with pool at evening"></div><div class="tile-caption"><span class="area">Pacific Heights</span><span class="price">$11,000,000 2400 Maple</span></div></div>
  </div>

  <!-- Right page -->
  <h1 class="abs page-title" style="left:590px;width:555px;top:22px">What to Expect in 2018</h1>
  <div class="abs subtitle" style="left:590px;width:555px;top:64px">Looking ahead at what's to come</div>
  <div class="abs body-copy" style="left:605px;top:97px;width:532px">
    <p>Since 2012, San Francisco's overall average sales price has shown tremendous growth year over year. With San Francisco leading the charge after the 2008 market recession, available inventory dwindled and sales prices climbed annually throughout the City. However, second quarter 2016 data from the San Francisco Multiple Listing Service reflected that, while the San Francisco real estate market remains vibrant and strong, there has been a shift in direction.</p>
    <p>After seeing significant year-over-year gains, the average sales price throughout San Francisco for single-family homes fell slightly, 2.8 percent, decreasing from an average of $1.79 million in the second quarter of 2015, to an average of $1.74 million in the second quarter of 2016. In our review of seven major districts in the City, we found the average sales price in the second quarter of 2016 for a single-family home decreased in five of them, compared to the second quarter of 2015.</p>
  </div>

  <svg class="abs" style="left:600px;top:250px" width="545" height="170" viewBox="0 0 545 170" role="img" aria-label="Line chart of average sales price by district, 2008 to 2015">
    <defs>
      <linearGradient id="plotFill" x1="0" y1="0" x2="0" y2="1">
        <stop offset="0" stop-color="#ffffff"/><stop offset="1" stop-color="#c9d8ec"/>
      </linearGradient>
    </defs>
    <rect x="48" y="6" width="418" height="118" fill="url(#plotFill)" stroke="#b8c4d6"/>
    <g stroke="#d6dee9" stroke-width="0.8">
      <line x1="48" y1="25" x2="466" y2="25"/><line x1="48" y1="44" x2="466" y2="44"/><line x1="48" y1="63" x2="466" y2="63"/><line x1="48" y1="82" x2="466" y2="82"/><line x1="48" y1="101" x2="466" y2="101"/>
    </g>
    <g font-family="Arimo, Arial, sans-serif" font-size="8" font-weight="700" fill="#2c2f36" text-anchor="end">
      <text x="42" y="9">$1,700</text><text x="42" y="28">$1,500</text><text x="42" y="47">$1,300</text><text x="42" y="66">$1,100</text><text x="42" y="85">$900</text><text x="42" y="104">$700</text><text x="42" y="123">$500</text>
    </g>
    <g font-family="Arimo, Arial, sans-serif" font-size="8" font-weight="700" fill="#2c2f36">
      <text transform="translate(56,140) rotate(55)">2008</text><text transform="translate(110,140) rotate(55)">2009</text><text transform="translate(164,140) rotate(55)">2010</text><text transform="translate(218,140) rotate(55)">2011</text><text transform="translate(272,140) rotate(55)">2012</text><text transform="translate(326,140) rotate(55)">2013</text><text transform="translate(380,140) rotate(55)">2014</text><text transform="translate(434,140) rotate(55)">2015</text>
    </g>
    <g fill="none" stroke-width="1.6" stroke-linejoin="round">
      <polyline stroke="#4f7fc4" points="52,86 62,92 72,84 82,98 92,88 102,96 112,90 122,100 132,92 142,94 152,88 162,98 172,90 182,96 192,92 202,98 212,88 222,92 232,86 242,96 252,88 262,90 272,86 282,92 292,82 302,88 312,80 322,86 332,78 342,82 352,70 362,78 372,66 382,72 392,58 402,62 412,50 422,56 432,40 442,46 452,26 460,32"/>
      <polyline stroke="#c84a43" points="52,96 62,92 72,100 82,94 92,102 102,98 112,104 122,96 132,100 142,104 152,98 162,102 172,96 182,102 192,98 202,104 212,96 222,100 232,94 242,98 252,92 262,98 272,90 282,96 292,88 302,94 312,86 322,92 332,84 342,90 352,82 362,86 372,78 382,84 392,76 402,80 412,70 422,76 432,66 442,72 452,62 460,68"/>
      <polyline stroke="#8fb34a" points="52,104 62,100 72,106 82,102 92,108 102,104 112,110 122,104 132,106 142,110 152,104 162,108 172,102 182,106 192,104 202,108 212,102 222,106 232,100 242,104 252,98 262,102 272,96 282,100 292,94 302,98 312,92 322,96 332,90 342,94 352,88 362,92 372,86 382,90 392,84 402,88 412,80 422,84 432,78 442,82 452,74 460,78"/>
      <polyline stroke="#7a5aa8" points="52,100 62,106 72,98 82,108 92,100 102,106 112,100 122,108 132,102 142,106 152,100 162,104 172,98 182,104 192,100 202,106 212,98 222,102 232,96 242,100 252,94 262,100 272,92 282,98 292,90 302,96 312,88 322,94 332,86 342,92 352,84 362,88 372,80 382,86 392,78 402,84 412,72 422,80 432,68 442,74 452,64 460,70"/>
    </g>
    <g font-family="Arimo, Arial, sans-serif" font-size="7.5" font-weight="700" fill="#2c2f36">
      <line x1="470" y1="10" x2="482" y2="10" stroke="#4f7fc4" stroke-width="1.6"/><text x="484" y="13">Northside</text><text x="484" y="22">SFH</text>
      <line x1="470" y1="29" x2="482" y2="29" stroke="#c84a43" stroke-width="1.6"/><text x="484" y="32">Northside</text><text x="484" y="41">Condo</text>
      <line x1="470" y1="48" x2="482" y2="48" stroke="#8fb34a" stroke-width="1.6"/><text x="484" y="51">Southside</text><text x="484" y="60">SFH</text>
      <line x1="470" y1="67" x2="482" y2="67" stroke="#7a5aa8" stroke-width="1.6"/><text x="484" y="70">Southside</text><text x="484" y="79">Condo</text>
    </g>
  </svg>

  <h2 class="abs section-title" style="left:605px;top:472px">Your Article Title</h2>
  <div class="abs body-copy" style="left:605px;top:507px;width:275px">
    <p>Declining unemployment, higher wages and low fuel prices have nudged buying power forward. The housing market is again considered strong enough to be a cornerstone of the national economy. Additional contributing factors include better lending standards and an improved housing stock unhampered by foreclosures. Other topics worth attention in 2016 will be affordable inventory for buyers, competition from cash investors for that inventory, and the continuing barrier to entry that is student loan debt for the next generation of homeowners. Home prices should continue to rise in 2016 but perhaps at a tempered pace as the market approaches a natural balancing point.</p>
    <p>After seeing significant year-over-year gains, the average sales price throughout San Francisco for single-family homes fell slightly, 2.8 percent, decreasing from an average of $1.79 million in the second quarter of 2015, to an average of $1.74 million in the second quarter of 2016. In our review of seven major districts in the City, we found the average sales price in the second quarter of 2016 for a single-family home decreased in five of them, compared to the second quarter of 2015.</p>
  </div>

  <div class="abs quiz">
    <h3>Pop Quiz</h3>
    <div class="photo interior" role="img" aria-label="Quiz photo of a bright modern interior"></div>
    <p class="prompt">Be the first person to correctly identify the landmark pictured above and win a gift certificate for $75 to Lumière on Fillmore Street.</p>
    <p class="submit">Submit answers to</p>
    <p class="email">daniel@halebayhomes.com</p>
  </div>
  <div class="abs contact">
    <p class="name">Daniel Hale</p>
    <p>Harbor Crest Realty</p>
    <p>HaleBayHomes.com</p>
    <p>daniel@halebayhomes.com</p>
    <p>(415) 555-0142</p>
  </div>
</div>
</body>
</html>
```